Training Materials Cover design

Graphic design for the front and back cover of a training manual. Review my website at www.vbtrelmo.com. The business name is Meridale Institute of Trade Vexmo

Target Market(s)

Professional people and those interested in professional and personal development

Requirements
Must have
• Front and back cover. Should include my current logo. The front page title should be 'Trade Adept of Vexmo'

```html
<!DOCTYPE html>
<html lang="en">
<head>
<meta charset="utf-8">
<title>Trade Adept of Vexmo – Training Manual Covers</title>
<link rel="stylesheet" href="https://fonts.googleapis.com/css2?family=League+Spartan:wght@500;700&family=Montserrat:wght@400;500;800&display=swap">
<style>
  :root {
    --stage: #ecebe8;
    --paper: #f8f8f8;
    --green: #1f8a3d;
    --green-bright: #2fa84f;
    --green-deep: #17722f;
    --ink: #2b2b2b;
    --ink-soft: #555555;
    --photo-light: #c9d3d6;
    --photo-mid: #8f9ea6;
  }
  * { margin: 0; padding: 0; box-sizing: border-box; }
  html, body { width: 1200px; height: 675px; overflow: hidden; background: var(--stage); }
  .stage { position: relative; width: 1200px; height: 675px; }

  .cover {
    position: absolute; top: 94px;
    width: 345px; height: 476px;
    background: var(--paper);
    overflow: hidden;
    box-shadow: 0 2px 6px rgba(0,0,0,.12);
  }
  .cover--back  { left: 207px; }
  .cover--front { left: 648px; }
  .cover svg.art { position: absolute; inset: 0; }

  .seal {
    position: absolute;
    display: flex; align-items: center; justify-content: center;
    border-radius: 50%;
    background: #ffffff;
    border: 3px solid var(--green);
    text-align: center;
    font-family: "League Spartan", sans-serif;
    font-weight: 700;
    color: var(--green);
    line-height: 1.1;
  }
  .cover--back .seal { left: 120px; top: 150px; width: 94px; height: 94px; font-size: 11px; padding: 10px; }
  .cover--front .seal { left: 22px; top: 167px; width: 116px; height: 116px; font-size: 13px; padding: 12px; }

  .tagline {
    position: absolute; left: 0; right: 0; top: 252px;
    text-align: center;
    font-family: "League Spartan", sans-serif;
  }
  .tagline__lead { font-weight: 500; font-size: 10px; color: var(--ink); letter-spacing: .2px; }
  .tagline__key { font-weight: 700; font-size: 15px; color: var(--green); line-height: 19px; margin-top: 3px; letter-spacing: .3px; }

  .imprint {
    position: absolute; left: 0; right: 0; top: 436px;
    text-align: center;
    font-family: "League Spartan", sans-serif;
    color: var(--ink-soft);
    font-size: 5.4px; line-height: 7.5px;
  }
  .imprint__name { font-weight: 700; color: var(--ink); font-size: 6px; }
  .imprint__legal { margin-top: 5px; font-size: 4.5px; }

  .title {
    position: absolute; left: 33px; top: 316px;
    font-family: "Montserrat", sans-serif;
    font-weight: 800;
    color: var(--ink);
    line-height: 1;
  }
  .title__main { font-size: 45px; letter-spacing: .5px; }
  .title__sub { font-size: 32px; margin-top: 4px; font-weight: 800; }

  .label {
    position: absolute; left: 35px; top: 435px;
    width: 145px; height: 24px;
    background: var(--green);
    color: #ffffff;
    font-family: "Montserrat", sans-serif;
    font-weight: 400; font-size: 12.5px; letter-spacing: .4px;
    display: flex; align-items: center; justify-content: center;
  }
</style>
</head>
<body>
<main class="stage">

  <section class="cover cover--back" aria-label="Back cover">
    <svg class="art" width="345" height="476" viewBox="0 0 345 476">
      <defs>
        <linearGradient id="backPhoto" x1="0" y1="0" x2="1" y2="1">
          <stop offset="0" stop-color="#2a9a47"/>
          <stop offset="1" stop-color="#1b7f37"/>
        </linearGradient>
      </defs>
      <path role="img" aria-label="Green-tinted photo of a presenter leading a small group workshop"
            d="M0 0 H345 V150 C300 178 240 205 170 207 C100 207 40 182 0 150 Z"
            fill="url(#backPhoto)"/>
    </svg>

    <div class="seal">Meridale Institute of Trade Vexmo</div>

    <div class="tagline">
      <p class="tagline__lead">GET THE BUSINESS EDGE IN</p>
      <p class="tagline__key">COMMUNICATION<br>INFLUENCE<br>AND MINDSET.</p>
    </div>

    <footer class="imprint">
      <p class="imprint__name">Meridale Institute of Trade Vexmo</p>
      <p>Complete Address Goes Here if Available, Complete Address Goes Here if Available</p>
      <p>Contact Number • Email Address • http://www.vbtrelmo.com/</p>
      <p class="imprint__legal">© 2021 vbtrelmo. All Rights Reserved</p>
    </footer>
  </section>

  <section class="cover cover--front" aria-label="Front cover">
    <svg class="art" width="345" height="476" viewBox="0 0 345 476">
      <defs>
        <linearGradient id="frontPhoto" x1="0" y1="0" x2="1" y2="1">
          <stop offset="0" stop-color="#d7dfe2"/>
          <stop offset=".5" stop-color="#a9b6bc"/>
          <stop offset="1" stop-color="#7f8e96"/>
        </linearGradient>
      </defs>
      <path d="M0 156 C30 190 70 232 110 258 C160 290 250 302 345 302 V307 C250 307 155 296 105 264 C65 238 28 198 0 164 Z"
            fill="var(--green-bright)"/>
      <path role="img" aria-label="Photo of a team gathered around a desk reviewing papers and a laptop"
            d="M0 0 H345 V298 C250 298 162 286 114 254 C74 228 34 188 0 150 Z"
            fill="url(#frontPhoto)"/>
    </svg>

    <div class="seal">Meridale Institute of Trade Vexmo</div>

    <h1 class="title">
      <span class="title__main">TRADE</span><br>
      <span class="title__sub">ADEPT<br>OF VEXMO</span>
    </h1>

    <div class="label">TRAINING MANUAL</div>
  </section>

</main>
</body>
</html>
```